Design for a real estate wev portal

Contents and features of the site
---------------------------------
Website in 5 languages: French, Dutch, English, German, Spanish.
English name of the site: Lantern Nest Living
Main purpose of the site:
- allow people to rent their house/ appartment for flatsharing purposes.
- help people wanting to find a room in flatsharing
- help people to find additional roommates for their flatsharing
Key interaction sequence:
1. I create a "group" of people who have common interest/hobbies
2. People who have the same interests/hobbies join my group
3. I look for a house/appartment to host my group
Website structure will be the following:
- Home
- Groups
-- Look for a group
--- Join a group
-- Create a group
- Properties
-- Look for a house/appartement
-- Apply
- Sales conditions
- Contact
- My account
-- My profile
-- My groups OR my properties
Your mission
------------
The client has no graphical guidelines, simply a logo (see attached).
We need a (responsive compliant) design for the following pages (we expect PSD's from you. No HTML nor CSS):
1. homepage (see example and wireframe attached)
2. properties search result list (see wireframe attached)
3. "detailed" form for properties
4. groups search result list
5. "detailed" form for groups
6. my account page
FOR THE COMPETITION step we only expect from you the design of first 2 screens.
Based on that, we will select the designer who will win the project, and will have to design the 4 remaining screens.
Target Market(s)
B2C
Industry/Entity Type
Real Estate
Number of Pages Required
5+ page
Look and feel
Each slider illustrates characteristics of the customer's brand and the style your logo design should communicate.

```html
<!DOCTYPE html>
<html lang="en">
<head>
<meta charset="utf-8">
<title>Lantern Nest Living</title>
<link href="https://fonts.googleapis.com/css2?family=Lato:wght@300;400;700&display=swap" rel="stylesheet">
<style>
:root{
  --green:#2f7a1c;
  --green-dark:#27691a;
  --green-card:#3d8a26;
  --teal:#0f5d6b;
  --teal-card:#176f7c;
  --teal-text:#0d5a66;
  --ink:#222;
  --muted:#666;
  --faq-bg:#eef2f7;
  --footer:#1c2427;
  --footer-2:#262f33;
  --pink:#e85fa8;
  --blue:#5a8de0;
  --badge:#1e9fe0;
  --mint:#8fd8a8;
  --yellow:#e8f27a;
}
*{box-sizing:border-box;margin:0;padding:0}
html,body{width:903px;height:1200px;overflow:hidden}
body{font-family:'Lato',sans-serif;color:var(--ink);background:#fff;position:relative}
.abs{position:absolute}

/* header */
.site-header{position:absolute;left:0;top:0;width:903px;height:52px;background:#fff}
.nav a{position:absolute;top:24px;font-size:6.5px;font-weight:700;color:#222;text-decoration:none;letter-spacing:.2px}
.nav .home{left:176px;top:22px}
.nav .home-bar{position:absolute;left:176px;top:40px;width:8px;height:1.5px;background:var(--green)}
.brand{position:absolute;left:382px;top:16px;width:140px;display:flex;align-items:center;gap:5px;justify-content:center}
.brand .dot{width:9px;height:9px;border-radius:50%;background:var(--green)}
.brand span{font-size:11px;font-weight:700;color:var(--green-dark)}

/* hero */
.hero{position:absolute;top:52px;left:0;width:903px;height:640px}
.half{position:absolute;top:0;height:640px;width:452px}
.half.left{left:0;background:linear-gradient(180deg,#4f8c3a 0%,#3b8224 30%,var(--green) 55%)}
.half.right{left:452px;width:451px;background:linear-gradient(180deg,#2e6f7a 0%,#176774 30%,var(--teal) 55%)}
.hero-icon{position:absolute;top:14px;width:40px;height:40px;border-radius:50%;display:flex;align-items:center;justify-content:center}
.left .hero-icon{left:289px;background:#4aa32c}
.right .hero-icon{left:123px;background:#1c7e8c}
.hero-title{position:absolute;top:60px;width:100%;font-size:11.5px;color:#fff;font-weight:400}
.left .hero-title{left:0;padding-left:177px;width:440px;text-align:center;padding-left:177px}
.right .hero-title{left:12px;width:274px;text-align:center}

.tile{position:absolute;top:89px;width:126px;height:125px;overflow:hidden}
.tile .photo{height:97px}
.tile .cap{height:28px;display:flex;align-items:center;justify-content:space-between;padding:0 9px;color:#fff;font-size:7px;line-height:1.2}
.left .tile .cap{background:var(--green-card)}
.right .tile .cap{background:var(--teal-card)}
.arrow-c{width:12px;height:12px;flex:none}

.spot{position:absolute;top:229px;width:263px;height:207px;background:#fff;box-shadow:0 1px 3px rgba(0,0,0,.25)}
.spot h4{font-size:5.5px;text-align:center;margin-top:13px;font-weight:700;letter-spacing:.2px}
.spot .rule{position:absolute;left:17px;right:17px;height:1px;background:#ddd}
.item{position:absolute;left:18px;right:18px;height:56px}
.item .thumb{position:absolute;left:0;top:0;width:69px;height:55px}
.item .body{position:absolute;left:79px;top:2px;right:0}
.item .name{font-size:7.2px;font-weight:700}
.left .item .name{color:var(--green)}
.right .item .name{color:var(--teal-text)}
.item p{font-size:5.8px;color:#555;line-height:1.6;margin-top:3px;width:110px}
.item .age{font-size:4.3px;color:#777;margin-top:5px}
.item .age b{color:#333}
.avatars{position:absolute;right:0;top:2px;display:flex;gap:3px}
.av{width:14px;height:14px;border-radius:1px;display:flex;align-items:center;justify-content:center}
.meta{font-size:6px;color:#555;display:flex;align-items:center;gap:6px;margin-top:4px}
.tag{display:inline-block;margin-top:6px;background:var(--badge);color:#fff;font-size:4.2px;font-weight:700;padding:2px 4px;border-radius:1px}
.spot .more{position:absolute;left:0;right:0;bottom:0;height:28px;background:#e3e6ea;display:flex;align-items:center;justify-content:center;font-size:5.2px;font-weight:700}
.left .spot .more{color:var(--green)}
.right .spot .more{color:var(--teal-text)}

.ksp{position:absolute;top:499px;text-align:center;color:#fff}
.ksp h3{font-size:11.5px;font-weight:400;color:var(--yellow)}
.ksp p{font-size:6.1px;line-height:1.4;margin-top:6px}

/* faq */
.faq{position:absolute;top:692px;left:0;width:903px;height:332px;background:var(--faq-bg)}
.faq-icon{position:absolute;left:429px;top:25px;width:46px;height:46px;border-radius:50%;background:var(--mint);display:flex;align-items:center;justify-content:center}
.faq h2{position:absolute;top:84px;width:100%;text-align:center;font-size:11.5px;font-weight:400;color:#222}
.faq h2 em{font-style:normal;color:var(--green)}
.q{position:absolute;left:238px;width:428px;height:41px;border-bottom:1px solid #cfd5dc;display:flex;align-items:center}
.q:first-of-type{border-top:1px solid #cfd5dc}
.q .n{width:23px;padding-left:8px;font-size:7.5px}
.q p{flex:1;font-size:7.5px;line-height:1.4;color:#333;padding-right:24px}
.q .go{width:20px;height:20px;flex:none;margin-right:3px}
.see-all{position:absolute;left:407px;top:270px;width:88px;height:19px;border:1px solid #999;background:#fff;font-size:6px;display:flex;align-items:center;justify-content:center;gap:8px}

/* footer */
.site-footer{position:absolute;top:1024px;left:0;width:903px;height:176px;background:var(--footer);color:#b8c0c4}
.f-title{position:absolute;top:38px;font-size:7px;color:#dde3e6;letter-spacing:.2px}
.f-line{position:absolute;top:53px;width:33px;height:1px;background:var(--green)}
.f-links{position:absolute;top:68px;font-size:6.3px;line-height:14px;color:#8c979c;list-style:none}
.search{position:absolute;left:177px;top:56px;display:flex;height:24px;font-size:6px}
.search .kw{width:88px;background:var(--footer-2);color:#5e6a70;display:flex;align-items:center;padding-left:8px}
.search .sel{width:83px;background:#2c3539;border-left:1px solid #1c2427;color:#ccd;display:flex;align-items:center;justify-content:space-between;padding:0 8px}
.search .btn{width:54px;margin-left:8px;background:var(--green);color:#dfe;display:flex;align-items:center;justify-content:center;font-size:6.5px}
.copy{position:absolute;bottom:14px;width:100%;text-align:center;font-size:4.5px;color:#55626a}
.bottom-rule{position:absolute;left:0;right:0;top:144px;height:1px;background:#222c30}
</style>
</head>
<body>

<header class="site-header">
  <nav class="nav">
    <a class="home" href="#"><svg width="7" height="7" viewBox="0 0 10 10"><path d="M1 5 5 1l4 4v4H6V6H4v3H1z" fill="#2f7a1c"/></svg></a>
    <span class="home-bar"></span>
    <a href="#" style="left:196px">GROUP ⌄</a>
    <a href="#" style="left:235px">PROPERTIES ⌄</a>
    <a href="#" style="left:291px">SALES CONDITIONS</a>
    <a href="#" style="left:662px">LOGIN</a>
    <a href="#" style="left:697px">REGISTER</a>
  </nav>
  <div class="brand"><i class="dot"></i><span>Lantern Nest Living</span></div>
</header>

<section class="hero">
  <div class="half left">
    <div role="img" aria-label="Background photo of young roommates laughing together" class="abs" style="inset:0 0 300px 0;background:linear-gradient(180deg,rgba(120,160,90,.35),rgba(47,122,28,0))"></div>
    <div class="hero-icon"><svg width="22" height="22" viewBox="0 0 24 24" fill="none" stroke="#fff" stroke-width="1.4"><circle cx="10" cy="10" r="7"/><path d="M15 15l6 6M6.5 10.5 10 7l3.5 3.5V13h-7z"/></svg></div>
    <div class="hero-title" style="left:0;padding:0;width:628px;text-align:center;left:0">Searching for Accomodation</div>

    <div class="tile" style="left:177px">
      <div class="photo" role="img" aria-label="Photo of a woman unpacking in a furnished room" style="background:linear-gradient(135deg,#7a5a3a,#3a8a9a)"></div>
      <div class="cap"><span>I want to rent a room<br>right now !</span><svg class="arrow-c" viewBox="0 0 12 12" fill="none" stroke="#fff"><circle cx="6" cy="6" r="5.3"/><path d="M3.5 6h5M6.5 4l2 2-2 2"/></svg></div>
    </div>
    <div class="tile" style="left:313px">
      <div class="photo" role="img" aria-label="Photo of friends sharing drinks at a party" style="background:linear-gradient(135deg,#2a1a12,#8a5a30)"></div>
      <div class="cap"><span>I want to join a group</span><svg class="arrow-c" viewBox="0 0 12 12" fill="none" stroke="#fff"><circle cx="6" cy="6" r="5.3"/><path d="M3.5 6h5M6.5 4l2 2-2 2"/></svg></div>
    </div>

    <div class="spot" style="left:177px">
      <h4>UNDER THE SPOTLIGHT</h4>
      <span class="rule" style="top:28px"></span>
      <div class="item" style="top:36px">
        <div class="thumb" role="img" aria-label="Photo of young workers chatting at a table" style="background:linear-gradient(135deg,#c9a070,#6a4a30)"></div>
        <div class="body">
          <div class="name">A NICE GROUP</div>
          <p>Young workers, seeking for accomodation downtown.</p>
          <div class="age">AVERAGE AGE: <b>35 YEARS</b></div>
        </div>
        <div class="avatars">
          <span class="av" style="background:var(--pink)"><svg width="8" height="8" viewBox="0 0 10 10" fill="#fff"><circle cx="5" cy="3.3" r="2.2"/><path d="M1 10a4 4 0 0 1 8 0z"/></svg></span>
          <span class="av" style="background:var(--blue)"><svg width="8" height="8" viewBox="0 0 10 10" fill="#fff"><circle cx="5" cy="3.3" r="2.2"/><path d="M1 10a4 4 0 0 1 8 0z"/></svg></span>
        </div>
      </div>
      <span class="rule" style="top:98px"></span>
      <div class="item" style="top:106px">
        <div class="thumb" role="img" aria-label="Photo of young women sitting on a sofa" style="background:linear-gradient(135deg,#3a3530,#d8d0c8)"></div>
        <div class="body">
          <div class="name">ANOTHER NICE GROUP</div>
          <p>Young ladies, studying at University seeking for accomodation close to Brussels University</p>
          <div class="age">AVERAGE AGE: <b>20 YEARS</b></div>
        </div>
        <div class="avatars">
          <span class="av" style="background:var(--pink)"><svg width="8" height="8" viewBox="0 0 10 10" fill="#fff"><circle cx="5" cy="3.3" r="2.2"/><path d="M1 10a4 4 0 0 1 8 0z"/></svg></span>
        </div>
      </div>
      <div class="more">SEE MORE GROUPS &nbsp;&gt;&gt;</div>
    </div>

    <div class="ksp" style="left:177px;width:263px">
      <h3>Key Selling Points for The Roommates</h3>
      <p>Lorem ipsum dolor sit amet, consectetur adipiscing elit, sed do eiusmod tempor incididunt ut labore et dolore magna aliqua. Ut enim ad minim veniam, quis nostrud exercitation ullamco laboris nisi ut aliquip ex ea commodo consequat.</p>
    </div>
  </div>

  <div class="half right">
    <div role="img" aria-label="Background photo of a bright living room interior" class="abs" style="inset:0 0 300px 0;background:linear-gradient(180deg,rgba(110,150,160,.35),rgba(15,93,107,0))"></div>
    <div class="hero-icon"><svg width="22" height="22" viewBox="0 0 24 24" fill="none" stroke="#fff" stroke-width="1.3"><path d="M3 11 11 4l8 7M5 10v9h10"/><circle cx="17" cy="17" r="4"/><path d="M17 15v4"/></svg></div>
    <div class="hero-title">I Have a House for Rent</div>

    <div class="tile" style="left:12px">
      <div class="photo" role="img" aria-label="Photo of hands typing on a laptop" style="background:linear-gradient(135deg,#9a8a80,#d8d8d8)"></div>
      <div class="cap"><span>I want to advertise !</span><svg class="arrow-c" viewBox="0 0 12 12" fill="none" stroke="#fff"><circle cx="6" cy="6" r="5.3"/><path d="M3.5 6h5M6.5 4l2 2-2 2"/></svg></div>
    </div>
    <div class="tile" style="left:148px">
      <div class="photo" role="img" aria-label="Photo of a woman standing in a sunny home office" style="background:linear-gradient(135deg,#c8c0b0,#4a4a4a)"></div>
      <div class="cap"><span>Why is flatsharing<br>interesting for me ?</span><svg class="arrow-c" viewBox="0 0 12 12" fill="none" stroke="#fff"><circle cx="6" cy="6" r="5.3"/><path d="M3.5 6h5M6.5 4l2 2-2 2"/></svg></div>
    </div>

    <div class="spot" style="left:12px">
      <h4>UNDER THE SPOTLIGHT</h4>
      <span class="rule" style="top:28px"></span>
      <div class="item" style="top:36px">
        <div class="thumb" role="img" aria-label="Photo of a modern kitchen" style="background:linear-gradient(135deg,#d8d4cc,#3a2a20)"></div>
        <div class="body">
          <div class="name">HOUSE OF LOREM IPSUM</div>
          <div class="meta"><svg width="6" height="8" viewBox="0 0 6 8"><path d="M3 8S0 4.5 0 3a3 3 0 0 1 6 0C6 4.5 3 8 3 8z" fill="#8aa4c8"/></svg>London</div>
          <div class="meta"><svg width="7" height="7" viewBox="0 0 10 10"><path d="M1 5 5 1l4 4v4H1z" fill="#6cc070"/></svg>Rent per month</div>
          <span class="tag">AVAILABILITY</span>
        </div>
      </div>
      <span class="rule" style="top:98px"></span>
      <div class="item" style="top:106px">
        <div class="thumb" role="img" aria-label="Photo of a bright living room with a sofa" style="background:linear-gradient(135deg,#e8e4dc,#b89870)"></div>
        <div class="body">
          <div class="name">APARTMENT OF LOREM IPSUM</div>
          <div class="meta"><svg width="6" height="8" viewBox="0 0 6 8"><path d="M3 8S0 4.5 0 3a3 3 0 0 1 6 0C6 4.5 3 8 3 8z" fill="#8aa4c8"/></svg>Brussels</div>
          <div class="meta"><svg width="7" height="7" viewBox="0 0 10 10"><path d="M1 5 5 1l4 4v4H1z" fill="#6cc070"/></svg>Rent per month</div>
          <span class="tag">AVAILABILITY</span>
        </div>
      </div>
      <div class="more">SEE MORE HOUSES &nbsp;&gt;&gt;</div>
    </div>

    <div class="ksp" style="left:16px;width:263px">
      <h3>Key Selling Points for The Owners</h3>
      <p>Lorem ipsum dolor sit amet, consectetur adipiscing elit, sed do eiusmod tempor incididunt ut labore et dolore magna aliqua. Ut enim ad minim veniam, quis nostrud exercitation ullamco laboris nisi ut aliquip ex ea commodo consequat.</p>
    </div>
  </div>
</section>

<section class="faq">
  <div class="faq-icon"><svg width="26" height="26" viewBox="0 0 26 26"><path d="M13 2a11 11 0 1 0 6 20l4 2-1-5A11 11 0 0 0 13 2z" fill="#fff"/><text x="13" y="18" text-anchor="middle" font-family="Lato,sans-serif" font-weight="700" font-size="14" fill="#e0463a">?</text></svg></div>
  <h2>Everything you need to know about <em>Flatsharing</em></h2>
  <div class="q" style="top:120px;border-top:1px solid #cfd5dc"><span class="n">1</span><p>Sed ut perspiciatis unde omnis iste natus error sit voluptatem accusantium doloremque laudantium, totam rem aperiam, eaque ipsa quae ab illo inventore veritatis et quasi architecto ...</p><svg class="go" viewBox="0 0 20 20" fill="none" stroke="#2f7a1c"><circle cx="10" cy="10" r="9.3"/><path d="M8.5 6.5 12 10l-3.5 3.5"/></svg></div>
  <div class="q" style="top:161px"><span class="n">2</span><p>Duis aute irure dolor in reprehenderit in voluptate velit esse cillum dolore eu fugiat nulla pariatur. Excepteur sint occaecat cupidatat non proident, sunt in culpa qui officia deserunt ...</p><svg class="go" viewBox="0 0 20 20" fill="none" stroke="#2f7a1c"><circle cx="10" cy="10" r="9.3"/><path d="M8.5 6.5 12 10l-3.5 3.5"/></svg></div>
  <div class="q" style="top:202px;border-bottom:none"><span class="n">3</span><p>Nemo enim ipsam voluptatem quia voluptas sit aspernatur aut odit aut fugit, sed quia consequuntur magni dolores eos qui ratione voluptatem sequi nesciunt. Neque porro quis ...</p><svg class="go" viewBox="0 0 20 20" fill="none" stroke="#2f7a1c"><circle cx="10" cy="10" r="9.3"/><path d="M8.5 6.5 12 10l-3.5 3.5"/></svg></div>
  <div class="see-all">See all questions <span>›</span></div>
</section>

<footer class="site-footer">
  <div class="f-title" style="left:177px">PRE-DEFINED SEARCH</div>
  <div class="search">
    <div class="kw">Keyword is here ...</div>
    <div class="sel">Accomodation <span>⌄</span></div>
    <div class="btn">SEARCH</div>
  </div>
  <div class="f-title" style="left:452px">QUICK LINKS</div><span class="f-line" style="left:452px"></span>
  <ul class="f-links" style="left:452px"><li>Home</li><li>Sales Conditions</li><li>Contact</li></ul>
  <div class="f-title" style="left:539px">GROUPS</div><span class="f-line" style="left:539px"></span>
  <ul class="f-links" style="left:539px"><li>Look for a group</li><li>Create a group</li></ul>
  <div class="f-title" style="left:633px">PROPERTIES</div><span class="f-line" style="left:633px"></span>
  <ul class="f-links" style="left:633px"><li>Look for a house/apartment</li><li>Apply</li></ul>
  <span class="bottom-rule"></span>
  <div class="copy">Copyright 2016 LANTERN NEST LIVING. All rights reserved.</div>
</footer>

</body>
</html>
```